Company Letter head for real estate company

need company letter head
Updates

You can use the logo that I submitted. no need to create a new one

Requirements
Must have
• must have my address on it..38264 WINDMERE, CANTON, MI 48302-1175, INFO@MUVRO.CA

```html
<!DOCTYPE html>
<html lang="en">
<head>
<meta charset="utf-8">
<title>Muvro Letterhead</title>
<link rel="stylesheet" href="https://fonts.googleapis.com/css2?family=Open+Sans:wght@400;600&family=Roboto:wght@400&display=swap">
<style>
  :root {
    --backdrop: #dcdcdc;
    --paper: #f7f7f7;
    --body-text: #5e5e5e;
    --footer-text: #3f3f3f;
    --brand-green: #7ab83a;
    --brand-dark: #2b2b2b;
    --ink-placeholder: #e6e8ee;
  }
  html, body {
    margin: 0;
    padding: 0;
    width: 1153px;
    height: 1200px;
    overflow: hidden;
    background: var(--backdrop);
  }
  .letterhead {
    position: absolute;
    left: 166px;
    top: 30px;
    width: 820px;
    height: 1140px;
    background: var(--paper);
    box-shadow: 0 6px 22px rgba(0,0,0,0.12);
    font-family: "Open Sans", Arial, sans-serif;
    color: var(--body-text);
  }
  .brand {
    position: absolute;
    top: 96px;
    left: 0;
    width: 100%;
    display: flex;
    justify-content: center;
    align-items: center;
    gap: 14px;
  }
  .brand-dot {
    width: 34px;
    height: 34px;
    border-radius: 50%;
    background: var(--brand-green);
  }
  .brand-name {
    font-family: "Open Sans", Arial, sans-serif;
    font-weight: 600;
    font-size: 42px;
    letter-spacing: 3px;
    color: var(--brand-dark);
    line-height: 1;
  }
  .letter-body {
    position: absolute;
    top: 272px;
    left: 72px;
    width: 671px;
    font-size: 15.4px;
    line-height: 22px;
  }
  .letter-body p {
    margin: 0 0 22px 0;
    text-align: justify;
  }
  .letter-body .salutation,
  .letter-body .closing {
    text-align: left;
  }
  .signature {
    width: 100px;
    height: 92px;
    background: var(--ink-placeholder);
    border-radius: 6px;
    margin-top: 10px;
  }
  .contact-footer {
    position: absolute;
    top: 1035px;
    left: 0;
    width: 100%;
    text-align: center;
    font-family: "Roboto", Arial, sans-serif;
    font-size: 19.5px;
    line-height: 27px;
    color: var(--footer-text);
  }
  .contact-line {
    display: flex;
    justify-content: center;
    align-items: center;
    gap: 10px;
  }
  .contact-item {
    display: inline-flex;
    align-items: center;
    gap: 5px;
  }
  .contact-item svg {
    width: 17px;
    height: 17px;
    fill: var(--brand-green);
  }
</style>
</head>
<body>
  <main class="letterhead">
    <header class="brand">
      <span class="brand-dot"></span>
      <span class="brand-name">MUVRO</span>
    </header>

    <section class="letter-body">
      <p class="salutation">Dear customer,</p>
      <p>Lorem ipsum dolor sit amet, consectetur adipisicing elit, sed do eiusmod tempor incididunt ut labore et dolore magna aliqua. Ut enim ad minim veniam, quis nostrud exercitation ullamco laboris nisi ut aliquip ex ea commodo consequat. Duis aute irure dolor in reprehenderit in voluptate velit esse cillum dolore eu fugiat nulla pariatur. Excepteur sint occaecat cupidatat non proident, sunt in culpa qui officia deserunt mollit anim id est laborum.</p>
      <p>Lorem ipsum dolor sit amet, consectetur adipisicing elit, sed do eiusmod tempor incididunt ut labore et dolore magna aliqua. Ut enim ad minim veniam, quis nostrud exercitation ullamco laboris nisi ut aliquip ex ea commodo consequat. Duis aute irure dolor in reprehenderit in voluptate velit esse cillum dolore eu fugiat nulla pariatur. Excepteur sint occaecat cupidatat non proident, sunt in culpa qui officia deserunt mollit anim id est laborum.</p>
      <p>Lorem ipsum dolor sit amet, consectetur adipisicing elit, sed do eiusmod tempor incididunt ut labore et dolore magna aliqua. Ut enim ad minim veniam, quis nostrud exercitation ullamco laboris nisi ut aliquip ex ea commodo consequat. Duis aute irure dolor in reprehenderit in voluptate velit esse cillum dolore eu fugiat nulla pariatur. Excepteur sint occaecat cupidatat non proident, sunt in culpa qui officia deserunt mollit anim id est laborum.</p>
      <p>Lorem ipsum dolor sit amet, consectetur adipisicing elit, sed do eiusmod tempor incididunt ut labore et dolore magna aliqua. Ut enim ad minim veniam, quis nostrud exercitation ullamco laboris nisi ut aliquip ex ea commodo consequat. Duis aute irure dolor in reprehenderit.</p>
      <p class="closing">Yours Sincerely,</p>
      <div class="signature" role="img" aria-label="Handwritten signature of the sender"></div>
    </section>

    <footer class="contact-footer">
      <div class="address">38264 Windmere, Canton, MI 48302-1175,</div>
      <div class="contact-line">
        <span class="contact-item">
          <svg viewBox="0 0 24 24" aria-hidden="true"><path d="M6.6 10.8a15.1 15.1 0 0 0 6.6 6.6l2.2-2.2a1 1 0 0 1 1-.25 11.4 11.4 0 0 0 3.6.57 1 1 0 0 1 1 1V20a1 1 0 0 1-1 1A17 17 0 0 1 3 4a1 1 0 0 1 1-1h3.5a1 1 0 0 1 1 1c0 1.25.2 2.45.57 3.6a1 1 0 0 1-.25 1z"/></svg>
          555.214.0187
        </span>
        <span class="contact-item">
          <svg viewBox="0 0 24 24" aria-hidden="true"><path d="M2 5h20v14H2z M4 7v.4l8 5.3 8-5.3V7l-8 5.3z" fill-rule="evenodd"/></svg>
          info@muvro.ca
        </span>
        <span class="contact-item">
          <svg viewBox="0 0 24 24" aria-hidden="true"><circle cx="12" cy="12" r="10"/><path d="M12 2a10 10 0 0 1 0 20M2 12h20M12 2c-3 3-3 17 0 20" fill="none" stroke="#f7f7f7" stroke-width="1.4"/></svg>
          www.muvro.ca
        </span>
      </div>
    </footer>
  </main>
</body>
</html>
```